Nutritional & Gastrointestinal Health Consulting Service-Website design

We need a website design for a new health consulting service called "Bright Meadow" based in Perth, Australia.

We will be providing consulting services in the areas of:
1) Nutrition and Diet
2) Gastrointestinal Health (which means stomach & digestive system related health)

These consulting services will be provided by an Accredited Dietitian and a Paediatric Gastroenterologist.

We are open to creative ideas in terms of design, layout, fonts and colours. We also would love to see images of nature in the backdrop with families (adults with kids) having a good time, fresh fruits and vegetables displayed in a farmer's market or supermarket. 2 or 3 images should be sufficient. We would also definitely want our logo somewhere in the main page of website. The logo file is also attached. Please have a look at a website's design that we really liked. We would love to see designs inspired by that style. The website details are in the in the "nice to have priorities" section of this project brief.

We also would be looking at website designers with software coding skills so that if we like the design we can go ahead with the next step of coding.

The website design should communicate the purpose of the website and at the same time be simple, elegant and unique/eye-catching.

We look forward to receiving creative ideas for our website from you all. Good luck!

More details have been added to our project- for example: Logo, fonts style, must haves etc etc. Please view the updated project brief. Looking forward to receiving your fantastic ideas for our website. Thanking you

Hi, I have updated the colour preference. Will add the content preferences tomorrow. thanks

Hello all, I have now added a LOT more content to what we want in our website. It is very much in detail, so please carefully have a read through the entire project brief. If you have any questions write back to me and I will try to respond as quickly as I can. Last few days were busy so couldn't respond quickly to all of you who had send me designs/queries/questions. Thank you for your patience. I look forward to receiving fantastic designs from you all. Good Luck :-)

Target Market(s)

Adults based in western speaking countries aged 18 to 60 years

Industry/Entity Type

Software

Font styles to use
Sans Serif
Script

Colors
faa54b
acd036

Requirements
Must have
• The website must have the MAIN logo file attached. I have attached 3 files: 1) MAIN logo; 2) supplementary logo A ; 3) supplementary logo B

I have selected 2 colours from the colour scheme (see below)-(as the colour of our logo is that).
However we would also like to see LIGHT CHOCOLATE BROWN or CHOCOLATE BROWN colour used as the background colour of the website
Preferred WEBSITE CONTENT:
1) HOME PAGE:
Content required=
--Company Logo
--Dr Rowan Pellfry
Paediatric Gastroenterologist & Hepatologist
-Lena Pellfry.
Dietitian & Nutritionist
--Website Menu (either listed horizontally or vertically):
Once clicked on each name:

Under each of the Website Menu items we want the following Headings to be added

2) ABOUT US page:
Sub-heading under this: Qualification, Skills, Special Interest

3) SERVICES
ROWAN'S PAGE: Individual Consultation, Endoscopy procedures
Individual Consultation, Group Based Services, Food Diary, Food & Symptom Diary

4) FEES & REBATE: Content as below:
Please Note: Payment of full fees is required at the time of consultation and procedures. 48 hours notice is required for cancellation of appointments/non-attendance. Failure to provide this may result in a fee being incurred. Please call reception to find out the amount of fee charged for cancellation of appointments/non-attendance.
headings are:
Paediatric Gastroenterology:
Rowan's pge
Individual Consultation - Initial (upto 30 mins):
Review Consultation (upto 15 mins):
Endoscopy procedures - No Gap fees charged. Fees will be billed directly to Vitacover. If any queries, please contact reception.

lena's pge
sub heading:
Individual Consultation - Initial (upto 45 mins):
Individual Consultation - Review (upto 30 mins):

Concession-Individual Consultation -Initial (upto 45 mins):
Concession-Individual Consultation - Review (upto 30 mins):
Please Note: Concession applies for health care card holders & pensioners

Group Based Services: Pricing subject to the type of service provided. Please contact us for an obligation free quote.
Education Topics Include:
- Paediatric Nutrition (Introducing Solids, Fussy Eating, Healthy Eating)
- Pregnancy Nutrition, Gestational Diabetes, Breastfeeding/Lactation Nutrition
- Healthy Eating, Supermarket Shopping Tips, Nutrition Label Reading Tips, Healthier
sub heading under nutrition & diet:
-Vitacover:
--A rebate of $52.95 is available from Vitacover if an EPC ( Enhanced Primary Care)/Chronic Disease Management (CDM) plan is issued by your GP.
--All mandatory paperwork needs to be available at the time of making your appointment for your eligibility.
-Private Health Fund:
--Most private health funds provide rebate on dietetic appointments. However the rebate amount depends on your level of cover. Thus, please contact your health fund to determine your entitled rebate.
-KRB: Approved provider for KRB services

6) FOR DOCTORS: Bright Meadow Paediatric Gastroenterologist Referral Form
Bright Meadow Dietitian Referral form
7) LOCATIONS & CONTACT

Paediatric Gastroenterology & Hepatology Service
Suite 46
Fairholt Grange Larchmont Medical Centre
17 Oswin Talbot Pde,
MURDOCH, WA 6150
P: (08) 9462 3051
F: (08) 9462 7309

Nutrition & Diet Service
Suite 46
17 Oswin Talbot Pde,
MURDOCH, WA 6150
P: (08) 9462 3051
F: (08) 9462 7309

Quill Medical Centre
52-54 Tarrago Parkway,
MANDURAH, WA 6210
P: (08) 9728 4402
F: (08) 96274518
www.qmcbaylow.com.au

This page should have a webform that has following titles:
-Your Name
-Your Email
-Your Phone
-Message

8) NEWS & BLOG
Nice to have
• We liked the design style of the websites below:
https://www.wellvorn.example/

http://tummyplex.example/

But feel free to use your creativity too
Should not have
• Please do not use any body building or muscle building images

```html
<!DOCTYPE html>
<html lang="en">
<head>
<meta charset="utf-8">
<title>Bright Meadow – Paediatric Gastroenterology</title>
<link rel="stylesheet" href="https://fonts.googleapis.com/css2?family=Arimo:wght@400;700&display=swap">
<style>
  :root{
    --choc-dark:#5a3416;
    --page-tan:#ae9889;
    --box-brown:#82634f;
    --header-brown:#8c6b56;
    --content-light:#dcd1ca;
    --frame-white:#f4f1ee;
    --orange:#faa54b;
    --lime:#d8ef52;
    --green:#acd036;
    --title-brown:#5b3316;
    --link-brown:#6e4a2c;
    --ink:#000;
  }
  *{box-sizing:border-box;margin:0;padding:0}
  html,body{width:1200px;height:997px;overflow:hidden}
  body{font-family:"Arimo",Arial,sans-serif;color:var(--ink);position:relative;background:var(--choc-dark)}
  .backdrop{position:absolute;inset:0;background:radial-gradient(circle at 50% 40%,#6b4423,#532f14)}
  .page{position:absolute;left:35px;top:37px;width:1131px;height:922px;border:3px solid var(--frame-white);border-radius:14px;background:var(--page-tan)}
  .account-links{position:absolute;right:42px;top:8px;font-size:13px}
  .account-links a{color:var(--link-brown)}
  .account-links .sep{display:inline-block;width:1px;height:14px;background:#e8e0da;margin:0 8px;vertical-align:-2px}
  .masthead{position:absolute;left:213px;top:22px;width:700px;height:178px;border:3px solid var(--frame-white);border-radius:16px;background:var(--header-brown);display:flex;align-items:center;justify-content:center;gap:12px}
  .brand-dot{width:26px;height:26px;border-radius:50%;background:var(--orange)}
  .brand-name{font-size:34px;font-weight:700;color:var(--green)}
  .block{position:absolute;border:3px solid var(--frame-white);border-radius:8px;background:var(--box-brown)}
  .block-title{height:28px;line-height:26px;text-align:center;color:#fff;font-weight:700;font-size:15px;border-bottom:3px solid var(--frame-white)}
  .main-menu{left:24px;top:219px;width:224px;height:241px}
  .main-menu ul{list-style:circle;margin:21px 0 0 56px;color:#222}
  .main-menu li{font-size:13px;font-weight:700;line-height:15px;margin-bottom:3px;width:120px}
  .main-menu a.warm{color:var(--orange)}
  .main-menu a.fresh{color:var(--lime)}
  .user-login{left:877px;top:219px;width:224px;height:212px}
  .user-login form{padding:16px 14px 0 14px;color:#fff;font-size:13px;font-weight:700}
  .user-login label{display:block;margin-bottom:1px}
  .user-login .req{color:#e33}
  .user-login input.field{width:108px;height:20px;border:1px solid #999;font:13px "Arimo",Arial,sans-serif;padding:1px 3px;margin-bottom:11px}
  .user-login ul{margin:4px 0 0 20px;font-weight:400;color:#fff}
  .user-login ul a{color:var(--lime)}
  .user-login button{margin-top:14px;font:12px "Arimo",Arial,sans-serif;padding:2px 9px;border:1px solid #888;border-radius:2px;background:linear-gradient(#fafafa,#ddd)}
  .content{position:absolute;left:258px;top:219px;width:608px;height:639px;border:3px solid var(--frame-white);border-radius:8px;background:var(--content-light)}
  .breadcrumb{margin:5px 10px 0 10px;padding:0 0 4px 10px;border-bottom:3px solid #f0ece9;font-size:13px;font-weight:700}
  .breadcrumb a{color:var(--ink)}
  .page-title{margin:12px 0 0 11px;font-size:20px;color:var(--title-brown)}
  .article{margin:28px 24px 0 24px;font-size:13px;line-height:15px}
  .article h2{font-size:17px;line-height:17px;margin-bottom:16px}
  .article .lead{font-weight:700;margin-bottom:15px}
  .article h3{font-size:17px;text-decoration:underline;margin-bottom:16px}
  .article h4{font-size:15px;margin-bottom:14px}
  .article p.body{margin-bottom:16px}
  .article hr{border:0;border-top:3px solid #f0ece9;margin-top:28px}
  .footer{position:absolute;left:0;right:0;top:882px;text-align:center;font-size:13px;font-weight:700}
  .footer a{color:var(--ink)}
</style>
</head>
<body>
<div class="backdrop" role="img" aria-label="Hand-drawn fruit and vegetable pattern on chocolate brown"></div>
<div class="page">
  <nav class="account-links"><a href="#">Login</a><span class="sep"></span><a href="#">Register</a></nav>
  <header class="masthead"><span class="brand-dot"></span><span class="brand-name">Bright Meadow</span></header>

  <aside class="block main-menu">
    <div class="block-title">Main menu</div>
    <ul>
      <li><a class="warm" href="#">Home</a></li>
      <li><a class="warm" href="#">About Us</a></li>
      <li><a class="warm" href="#">Nutrition &amp; Diet</a></li>
      <li><a class="warm" href="#">Paediatric Gastroenterology</a></li>
      <li><a class="fresh" href="#">Fees &amp; Rebate</a></li>
      <li><a class="fresh" href="#">For Doctors</a></li>
      <li><a class="fresh" href="#">Location</a></li>
      <li><a class="fresh" href="#">Contact</a></li>
      <li><a class="fresh" href="#">News &amp; Blog</a></li>
    </ul>
  </aside>

  <main class="content">
    <div class="breadcrumb"><a href="#">Home</a></div>
    <h1 class="page-title">Paediatric Gastroenterology</h1>
    <div class="article">
      <h2>Individual consultation for gastrointestinal and liver disorders affecting children</h2>
      <p class="lead">Including conditions affecting the stomach, small intestine, large intestine/colon, rectum, anus, liver, biliary system and pancreas.</p>
      <h3>Endoscopy Procedures</h3>
      <h4>Gastroscopy</h4>
      <p class="body">Cras lobortis mattis justo, vehicula venenatis leo auctor pellentesque. Maecenas accumsan efficitur mauris, eu posuere quam bibendum at. Quisque a ullamcorper ex. Mauris placerat sem at suscipit mollis. Nulla facilisi. Nam porta placerat pulvinar. Aliquam ac ante consequat, euismod arcu in, tincidunt augue. In felis metus, rutrum sit amet dolor vel, rhoncus ultrices tortor.</p>
      <h4>Colonoscopy</h4>
      <p class="body">Suspendisse commodo sapien eget nunc gravida, in semper nisl commodo. Nulla quis quam vitae ex sodales efficitur id a nisi. Sed quis erat ac nunc accumsan feugiat ac sed ipsum. Vestibulum facilisis sem nec efficitur finibus. Vestibulum ex elit, vulputate vitae feugiat sit amet, consequat quis turpis. Etiam aliquet, quam ac ornare ultricies, urna magna maximus nibh, sit amet sodales orci mauris a arcu. Aliquam ornare ut enim sed sollicitudin.</p>
      <h4>Flexible Sigmoidoscopy</h4>
      <p class="body">Sed leo ante, eleifend vehicula tincidunt ac, imperdiet non purus. Morbi non enim a lacus suscipit suscipit. Vivamus fermentum, nunc in elementum placerat, nulla velit ullamcorper risus, et finibus turpis odio sed orci. In condimentum volutpat neque, at luctus orci varius at. Sed et porttitor risus, ac sollicitudin quam. Mauris bibendum suscipit eros a dignissim. Aenean aliquam turpis a quam viverra sollicitudin. Vestibulum vulputate leo id ante efficitur volutpat. Quisque a dolor egestas, luctus massa id, posuere velit. Donec nec ligula euismod, tempus massa ac, vulputate ex. Fusce in dictum sem.</p>
      <hr>
    </div>
  </main>

  <aside class="block user-login">
    <div class="block-title">User login</div>
    <form>
      <label>Username <span class="req">*</span></label>
      <input class="field" type="text" value="Tamsin">
      <label>Password <span class="req">*</span></label>
      <input class="field" type="password" value="passwordxyz">
      <ul><li><a href="#">Request new password</a></li></ul>
      <button type="button">Log in</button>
    </form>
  </aside>

  <footer class="footer"><a href="#">Bright Meadow</a> © Copyright 2014</footer>
</div>
</body>
</html>
```